Visitenkarten- und Briefpapier Design - Logo vorhanden!
Zielgruppe
Wir sind eine Projektentwicklungs GmbH die Grundstücke kauft, projektiert und wieder verkauft. Eine zukünftige GmbH ist für den Innenausbau von neuen Häusern (EFH,DHH,MFH) gedacht. Wir sind ebenfalls für den Vertrieb von Häusern tätig.
Unsere Zielgruppe sind Endkunden im Immobilienbereich die Grundstücke und/oder Häuser bis Schlüsselfertig kaufen möchten, sowie Grundstückseigentümer die verkaufen wollen.
Wir benötigen Visitenkarten UND Briefpapier.
Aufgabenstellung
Bitte vorhandenes Logo verwenden.
Briefpapier:
Es soll ein ansprechendes modernes Design sein. Wir lassen uns gerne überraschen und versuchen schnellstmöglich Feedback zu geben.
Visitenkarte:
Es soll ein ansprechendes modernes Design sein. Die Visitenkarte bitte mit 2 Seiten, auf der Rückseite könnten wir uns das Dunkle ZERANT Logo sehr gut vorstellen (nur Logo).

```html
<!DOCTYPE html>
<html lang="de">
<head>
<meta charset="utf-8">
<title>ZERANT – Visitenkarte und Briefpapier</title>
<link href="https://fonts.googleapis.com/css2?family=Roboto+Condensed:wght@300;400;700&display=swap" rel="stylesheet">
<style>
  :root {
    --board: #d2d2d2;
    --paper: #ffffff;
    --ink: #222222;
    --green: #86a843;
    --navy: #233a53;
    --sage: #9ba187;
    --shadow: 2px 3px 6px rgba(0,0,0,.28);
  }
  * { box-sizing: border-box; margin: 0; padding: 0; }
  html, body { width: 849px; height: 1200px; overflow: hidden; }
  body {
    background: var(--board);
    font-family: "Roboto Condensed", sans-serif;
    position: relative;
  }
  .set { position: absolute; left: 0; width: 849px; height: 395px; }
  .set--green { top: 0;   --brand: var(--green); }
  .set--navy  { top: 395px; --brand: var(--navy); }
  .set--sage  { top: 790px; --brand: var(--sage); }

  /* Card back */
  .card-back {
    position: absolute; left: 153px; top: 55px;
    width: 252px; height: 163px;
    background: var(--brand);
    transform: rotate(-5deg);
    box-shadow: var(--shadow);
    display: flex; align-items: center; justify-content: center;
  }
  .card-back .wordmark {
    color: var(--paper); font-size: 40px; font-weight: 400; letter-spacing: 2px;
  }

  /* Card front */
  .card-front {
    position: absolute; left: 189px; top: 205px;
    width: 252px; height: 164px;
    background: var(--paper);
    box-shadow: var(--shadow);
    overflow: hidden;
  }
  .card-front .field {
    position: absolute; inset: 0;
    background: var(--brand);
    clip-path: polygon(0 51px, 100% 68px, 100% 100%, 0 100%);
  }
  .card-front .wordmark {
    position: absolute; right: 16px; top: 26px;
    color: var(--brand); font-size: 20px; letter-spacing: 1px;
  }
  .name-tag {
    position: absolute; left: 0; top: 74px;
    width: 119px; height: 24px;
    background: var(--paper);
    transform: rotate(-1.2deg); transform-origin: left center;
    box-shadow: 1px 1px 3px rgba(0,0,0,.25);
    color: var(--brand);
    font-size: 15px; line-height: 24px; padding-left: 8px; letter-spacing: .3px;
    white-space: nowrap;
  }
  .name-tag strong { font-weight: 700; }
  .role {
    position: absolute; left: 8px; top: 101px;
    color: var(--paper); font-size: 7.5px; font-weight: 400; letter-spacing: .5px;
    transform: rotate(-1.2deg); transform-origin: left center;
  }
  .contact {
    position: absolute; right: 18px; top: 111px;
    color: var(--paper); font-size: 9px; line-height: 11.4px;
    text-align: right; font-weight: 400;
    padding-right: 7px; border-right: .6px solid var(--paper);
  }

  /* Letterhead */
  .letter {
    position: absolute; left: 495px; top: 62px;
    width: 208px; height: 294px;
    background: var(--paper);
    box-shadow: var(--shadow);
    overflow: hidden;
  }
  .letter .sender {
    position: absolute; left: 20px; top: 27px;
    width: 84px; height: 4.5px;
    background: var(--brand);
    color: var(--paper); font-size: 2.6px; line-height: 4.5px; padding-left: 2px;
    white-space: nowrap; overflow: hidden;
  }
  .letter .recipient {
    position: absolute; left: 20px; top: 39px;
    font-size: 4px; line-height: 5.4px; color: var(--ink);
  }
  .letter .wordmark {
    position: absolute; right: 15px; top: 30px;
    color: var(--brand); font-size: 16px; letter-spacing: 1px;
  }
  .letter .ghost {
    position: absolute; right: 6px; bottom: 46px;
    color: var(--brand); opacity: .08; font-size: 26px; letter-spacing: 1px;
  }
  .letter .band {
    position: absolute; inset: 0;
    background: var(--brand);
    clip-path: polygon(0 256px, 100% 270px, 100% 100%, 0 100%);
  }
  .letter .footer-tag {
    position: absolute; left: 0; top: 267px;
    width: 107px; height: 20px;
    background: var(--paper);
    transform: rotate(-1.5deg); transform-origin: left center;
    box-shadow: 1px 1px 2px rgba(0,0,0,.25);
    color: var(--brand); font-size: 2.6px; line-height: 3.4px; padding: 4px 0 0 10px;
    white-space: nowrap; overflow: hidden;
  }
  .footer-tag b { font-weight: 700; }
</style>
</head>
<body>

<section class="set set--green">
  <div class="card-back"><span class="wordmark">ZERANT</span></div>
  <div class="card-front">
    <div class="field"></div>
    <span class="wordmark">ZERANT</span>
    <div class="name-tag">JONAS <strong>KELLER.</strong></div>
    <div class="role">– GESCHÄFTSFÜHRUNG</div>
    <div class="contact">Lindenweg 118<br>31847 Weidental<br>01 76/ 58 12 90 47<br>jkeller@zerant.de</div>
  </div>
  <div class="letter">
    <div class="sender">ZERANT · Lindenweg 118 · Weidental</div>
    <div class="recipient">Max Mustermann<br>Musterstraße 44<br><br>43114 Musterstadt</div>
    <span class="wordmark">ZERANT</span>
    <span class="ghost">ZERANT</span>
    <div class="band"></div>
    <div class="footer-tag"><b>ZERANT GmbH</b><br>Lindenweg 118 · 31847 Weidental · 01 76/58 12 90 47 · info@zerant.de<br>IBAN DE00 1111 2222 3333 · Weidentaler Bank · www.zerant.de</div>
  </div>
</section>

<section class="set set--navy">
  <div class="card-back"><span class="wordmark">ZERANT</span></div>
  <div class="card-front">
    <div class="field"></div>
    <span class="wordmark">ZERANT</span>
    <div class="name-tag">JONAS <strong>KELLER.</strong></div>
    <div class="role">– GESCHÄFTSFÜHRUNG</div>
    <div class="contact">Lindenweg 118<br>31847 Weidental<br>01 76/ 58 12 90 47<br>jkeller@zerant.de</div>
  </div>
  <div class="letter">
    <div class="sender">ZERANT · Lindenweg 118 · Weidental</div>
    <div class="recipient">Max Mustermann<br>Musterstraße 44<br><br>43114 Musterstadt</div>
    <span class="wordmark">ZERANT</span>
    <span class="ghost">ZERANT</span>
    <div class="band"></div>
    <div class="footer-tag"><b>ZERANT GmbH</b><br>Lindenweg 118 · 31847 Weidental · 01 76/58 12 90 47 · info@zerant.de<br>IBAN DE00 1111 2222 3333 · Weidentaler Bank · www.zerant.de</div>
  </div>
</section>

<section class="set set--sage">
  <div class="card-back"><span class="wordmark">ZERANT</span></div>
  <div class="card-front">
    <div class="field"></div>
    <span class="wordmark">ZERANT</span>
    <div class="name-tag">JONAS <strong>KELLER.</strong></div>
    <div class="role">– GESCHÄFTSFÜHRUNG</div>
    <div class="contact">Lindenweg 118<br>31847 Weidental<br>01 76/ 58 12 90 47<br>jkeller@zerant.de</div>
  </div>
  <div class="letter">
    <div class="sender">ZERANT · Lindenweg 118 · Weidental</div>
    <div class="recipient">Max Mustermann<br>Musterstraße 44<br><br>43114 Musterstadt</div>
    <span class="wordmark">ZERANT</span>
    <span class="ghost">ZERANT</span>
    <div class="band"></div>
    <div class="footer-tag"><b>ZERANT GmbH</b><br>Lindenweg 118 · 31847 Weidental · 01 76/58 12 90 47 · info@zerant.de<br>IBAN DE00 1111 2222 3333 · Weidentaler Bank · www.zerant.de</div>
  </div>
</section>

</body>
</html>
```